PLUM BUSINESS CARD

Need a business card and logo. The company name is PLUM (Coastal Society of Junior Equestrian Arts). It's a business that offers horseback riding lessons to young girls. Please put my name: Marlene Tobbitt and a place for email and phone number. I would like the card to look feminine and soft. I like script type lettering. I want the card to be white or ivory with black or gray and hot pink print. A horse head outline would be cool, something whimsical. Think teen girl who likes glamour. Also, I give western riding lessons. So I like faded out background Images of western saddles, cowgirls, horses with long hair, ropes, horses in sunset...mabe the word PLUM can be made out of a lasso rope?

Just updated my project with a little more detail

Target Market(s)

Young girls/ cowgirls, western riding

Industry/Entity Type

Horseback Riding

Font styles to use
Script

Colors
e34197

Requirements
Must have
• A logo of PLUM.
Must say Coastal Society of Junior Equestrian Arts
Colors are Pink and Black with an elegant, glamorous, feminine look.
Nice to have
• Could have a picture or outline of a horse

```html
<!DOCTYPE html>
<html lang="en">
<head>
<meta charset="utf-8">
<title>PLUM Business Card</title>
<link rel="stylesheet" href="https://fonts.googleapis.com/css2?family=Marcellus&family=Pinyon+Script&family=Josefin+Sans:wght@600&display=swap">
<style>
  :root {
    --card-ivory: #fcf8f6;
    --wash-pink: #f2c3d0;
    --wash-pink-light: #f8dfe6;
    --hot-pink: #e34197;
    --ink-gray: #4a4a4a;
  }
  html, body {
    margin: 0;
    padding: 0;
    width: 1200px;
    height: 686px;
    overflow: hidden;
    background: var(--card-ivory);
  }
  .card {
    position: relative;
    width: 1200px;
    height: 686px;
    background: var(--card-ivory);
    overflow: hidden;
  }
  .watercolor-wash {
    position: absolute;
    left: 0;
    top: 0;
    width: 1200px;
    height: 686px;
  }
  .brand-name {
    position: absolute;
    left: 0;
    width: 1200px;
    top: 258px;
    margin: 0;
    text-align: center;
    font-family: "Marcellus", serif;
    font-weight: 400;
    font-size: 222px;
    line-height: 1;
    letter-spacing: 4px;
    color: var(--ink-gray);
  }
  .brand-tagline {
    position: absolute;
    left: 0;
    width: 1200px;
    top: 506px;
    margin: 0;
    text-align: center;
    font-family: "Pinyon Script", cursive;
    font-size: 44px;
    line-height: 1;
    color: var(--hot-pink);
  }
  .contact-line {
    position: absolute;
    left: 0;
    width: 1200px;
    top: 604px;
    margin: 0;
    text-align: center;
    font-family: "Josefin Sans", sans-serif;
    font-weight: 600;
    font-size: 19px;
    letter-spacing: 3px;
    text-transform: uppercase;
    color: var(--ink-gray);
  }
  .contact-line .divider {
    margin: 0 14px;
  }
  .contact-line .label {
    font-size: 16px;
  }
</style>
</head>
<body>
  <main class="card">
    <svg class="watercolor-wash" viewBox="0 0 1200 686" role="img" aria-label="Soft pink watercolor wash of a horse's flowing mane on the left side">
      <defs>
        <linearGradient id="wash-fade" x1="0" y1="0" x2="1" y2="0.3">
          <stop offset="0" stop-color="var(--wash-pink)" stop-opacity="0.9"/>
          <stop offset="0.6" stop-color="var(--wash-pink-light)" stop-opacity="0.7"/>
          <stop offset="1" stop-color="var(--wash-pink-light)" stop-opacity="0"/>
        </linearGradient>
      </defs>
      <path d="M0 40 C120 0 300 10 420 60 C520 100 560 180 600 260 C560 330 520 420 440 500 C360 580 240 640 120 686 L0 686 Z" fill="url(#wash-fade)"/>
    </svg>

    <h1 class="brand-name">PLUM</h1>
    <p class="brand-tagline">Coastal Society of Junior Equestrian Arts</p>
    <p class="contact-line">
      <span class="contact-name">Marlene Tobbitt</span><span class="divider">|</span><span class="label">Tel.</span> 555.208.4417<span class="divider">|</span><span class="label">E-mail:</span> m.tobbitt@plummail.com
    </p>
  </main>
</body>
</html>
```